New Business Card Design Project

I have a logo I would like to use on the business card. I want something that will stand out and that will be remembered.

Target Market(s)

People who collect gems, minerals and crystals.

Contact Information for Business Card

email - mkthestonefalcon@vendrollo.com
phone # 917-406-2581

Font styles to use
Serif
Sans Serif
Decorative

Colors

Designer to choose colors to be used in the design.

Requirements
Must have
• The logo...two to choose from.
Nice to have
• An eye catching and memorable way to draw in people who collect gems minerals and crystals.

```html
<!DOCTYPE html>
<html lang="en">
<head>
<meta charset="utf-8">
<title>The Stone Falcon – Business Card</title>
<link href="https://fonts.googleapis.com/css2?family=Montserrat:wght@400;500;700;800&display=swap" rel="stylesheet">
<style>
  :root {
    --page-bg: #e9e7e4;
    --card-bg: #fbfbfb;
    --ink: #1c1c1c;
    --brand-blue: #4453b0;
    --text-grey: #2a2a2a;
  }
  * { box-sizing: border-box; margin: 0; padding: 0; }
  html, body {
    width: 1200px; height: 960px; overflow: hidden;
    background: var(--page-bg);
    font-family: "Montserrat", sans-serif;
  }
  .card {
    position: absolute; left: 100px; top: 194px;
    width: 1000px; height: 572px;
    background: var(--card-bg);
    box-shadow: 0 10px 30px rgba(0,0,0,.18);
    overflow: hidden;
  }
  .brand {
    position: absolute; left: 40px; top: 0; width: 440px; height: 520px;
    display: flex; align-items: center; justify-content: center;
  }
  .brand-name {
    font-weight: 800; font-size: 46px; line-height: 1.05;
    color: var(--ink); text-align: center; text-transform: uppercase;
    letter-spacing: 1px;
  }
  .divider {
    position: absolute; left: 500px; top: 100px;
    width: 3px; height: 350px; background: var(--ink);
  }
  .details { position: absolute; left: 570px; top: 118px; }
  .person-name { font-weight: 700; font-size: 46px; color: var(--ink); }
  .person-title { font-weight: 500; font-size: 32px; color: var(--brand-blue); margin-top: 4px; }
  .contact-list { list-style: none; margin-top: 30px; }
  .contact-list li {
    display: flex; align-items: flex-start; gap: 16px;
    font-size: 22px; font-weight: 400; color: var(--text-grey);
    line-height: 1.3; margin-bottom: 8px;
  }
  .contact-list li.address { margin-top: 26px; font-size: 26px; }
  .contact-list svg { flex: none; width: 26px; height: 26px; fill: var(--brand-blue); margin-top: 2px; }
  .card-band { position: absolute; left: 0; bottom: 0; width: 1000px; height: 80px; }
</style>
</head>
<body>
  <div class="card">
    <div class="brand">
      <div class="brand-name">The Stone<br>Falcon</div>
    </div>

    <div class="divider"></div>

    <div class="details">
      <h1 class="person-name">Your Name</h1>
      <p class="person-title">Your Title</p>
      <ul class="contact-list">
        <li>
          <svg viewBox="0 0 24 24" aria-hidden="true"><path d="M6.6 10.8a15.1 15.1 0 0 0 6.6 6.6l2.2-2.2a1 1 0 0 1 1-.25 11.4 11.4 0 0 0 3.6.57 1 1 0 0 1 1 1V20a1 1 0 0 1-1 1A17 17 0 0 1 3 4a1 1 0 0 1 1-1h3.5a1 1 0 0 1 1 1c0 1.25.2 2.45.57 3.57a1 1 0 0 1-.25 1z"/></svg>
          917-406-2581
        </li>
        <li>
          <svg viewBox="0 0 24 24" aria-hidden="true"><path d="M2 5h20v14H2z M3.5 6.5v.4l8.5 6 8.5-6v-.4z" fill-rule="evenodd"/><path d="M3.5 8.6V17.5h17V8.6l-8.5 6z" fill="#fff" opacity=".0"/></svg>
          mkthestonefalcon@vendrollo.com
        </li>
        <li class="address">
          <svg viewBox="0 0 24 24" aria-hidden="true"><path d="M12 2a7 7 0 0 0-7 7c0 5 7 13 7 13s7-8 7-13a7 7 0 0 0-7-7zm0 9.5A2.5 2.5 0 1 1 12 6.5a2.5 2.5 0 0 1 0 5z"/></svg>
          <span>Your address, city<br>state, ZIP 0000</span>
        </li>
      </ul>
    </div>

    <svg class="card-band" viewBox="0 0 1000 80" aria-hidden="true">
      <polygon points="0,58 790,22 765,80 0,80" fill="var(--brand-blue)"/>
      <polygon points="812,20 1000,8 1000,80 786,80" fill="var(--ink)"/>
    </svg>
  </div>
</body>
</html>
```